Poster Design for Photography Exhibit

We are looking for a poster design for a photography exhibit featuring high-end fashion and celebrity photography.

Name of the exhibit is "MILES DORVAN: UNTITLED" (please use Helvetica Black all cap for show name.

Poster is LANDSCAPE format (2 units wide by 1 unit high).

Unfortunately due to legal reasons, we cannot use any actual Miles Dorvan photos. No can we use fashions or people on the poster!

We are looking for a high-end, sexy, bold provocative design that captures the excitement and glamour of a fashion photo shoot.

Target Market(s)

Men and Women interested in Fashion Photography and art photography in general

Industry/Entity Type

Fashion

Requirements
Must have
• landscape format, name of exhibit in Helvetica Black all caps
Nice to have
• Can be grayscale or color.
Should not have
• Logos or brand names

```html
<!DOCTYPE html>
<html lang="en">
<head>
<meta charset="utf-8">
<title>Miles Dorvan: Untitled — Photography Exhibit</title>
<link rel="stylesheet" href="https://fonts.googleapis.com/css2?family=Archivo+Black&family=Archivo:wght@800&display=swap">
<style>
  :root {
    --page: #ffffff;
    --ink: #1b1a1e;
    --accent-blue: #009de0;
    --title-white: #ffffff;
  }
  html, body {
    margin: 0;
    padding: 0;
    width: 1200px;
    height: 1000px;
    overflow: hidden;
    background: var(--page);
  }
  .poster {
    display: block;
    width: 1200px;
    height: 1000px;
  }
  .poster__field { fill: var(--ink); }
  .poster__name,
  .poster__title {
    font-family: "Archivo Black", "Helvetica Neue", Helvetica, Arial, sans-serif;
    font-weight: 900;
  }
  .poster__name { fill: var(--accent-blue); font-size: 118px; }
  .poster__title { fill: var(--title-white); font-size: 120px; }
  .poster__caption {
    font-family: "Archivo", "Helvetica Neue", Helvetica, Arial, sans-serif;
    font-weight: 800;
    font-size: 15px;
    fill: var(--title-white);
  }
</style>
</head>
<body>
<svg class="poster" viewBox="0 0 1200 1000" xmlns="http://www.w3.org/2000/svg" role="img" aria-label="Miles Dorvan: Untitled, photography exhibit poster">
  <rect class="poster__field" x="50" y="226" width="1094" height="545"/>

  <g class="poster__upright">
    <text class="poster__name" x="55" y="383" textLength="1085" lengthAdjust="spacingAndGlyphs">MILES DORVAN</text>
    <text class="poster__title" x="288" y="486" textLength="620" lengthAdjust="spacingAndGlyphs">UNTITLED</text>
  </g>

  <g class="poster__reflection" transform="translate(0 987) scale(1 -1)" aria-hidden="true">
    <text class="poster__name" x="55" y="383" textLength="1085" lengthAdjust="spacingAndGlyphs">MILES DORVAN</text>
    <text class="poster__title" x="288" y="486" textLength="620" lengthAdjust="spacingAndGlyphs">UNTITLED</text>
  </g>

  <text class="poster__caption" x="499" y="733" textLength="194" lengthAdjust="spacingAndGlyphs">PHOTOGRAPHY EXHIBIT</text>
</svg>
</body>
</html>
```